Following list to be designed:

1. A4 Letter Head

Must comprise of:
BRIGHT HARBOR and its LOGO
Address: No.41, 2F, Tarwin Plaza, Melrick Road, Upper Fenwood Gardens, Bangalore 560 017
Tel: 080 27481930
Fax: 080 27481931
Mail: query@brightharbor.example

Color of wordings to be in the lighter shade of blue and brighter shade of blue.

2. A4 Envelope

Must comprise of:
BRIGHT HARBOR and its LOGO
Tel: 080 27481930
Fax: 080 27481931

3. Postal Envelope

Must comprise of:
BRIGHT HARBOR and its LOGO
Tel: 080 27481930
Fax: 080 27481931

4. Business Card

Must comprise of:
Rohan Mehta
Managing Partner
Cell: +91 9487215043
Mail: rohanmehta@brightharbor.example
Tel: 080 27481930
Fax: 080 27481931

5. A4 Letter Head

Must comprise of:
BRIGHT HARBOR CORP. (wording) and BRIGHT HARBOR LOGO (only blue ribbon)

Blue ribbon (BRIGHT HARBOR LOGO) may be placed on Left Top Corner of the A4 Letter Head
and BRIGHT HARBOR CORP. (wording) to be placed on Right Top Corner of the A4 Letter Head

Tel: 080 27481930
Fax: 080 27481931

6. . A4 Envelope

Must comprise of:

Blue ribbon (BRIGHT HARBOR LOGO) may be placed on Left Top Corner of the A4 Envelope
and BRIGHT HARBOR CORP. (wording) to be placed on Right Top Corner of the A4 Envelope
Tel: 080 27481930
Fax: 080 27481931

Target Market(s)

Top IT/ITES Organizations

Industry/Entity Type

Real Estate Development

Font styles to use
Serif
Sans Serif

Colors
33a6d7
0792cd
85cae6

Requirements
Should not have
• Playful font and color

```html
<!DOCTYPE html>
<html lang="en">
<head>
<meta charset="utf-8">
<title>Bright Harbor Corp. Letterhead</title>
<link rel="stylesheet" href="https://fonts.googleapis.com/css2?family=Open+Sans:wght@400;600;700&display=swap">
<style>
  :root {
    --backdrop: #e9eaec;
    --paper: #ffffff;
    --ink: #2b2b2b;
    --wordmark: #3a3a3a;
    --blue-bright: #0792cd;
    --blue-mid: #33a6d7;
    --blue-light: #85cae6;
    --signature-tone: #d9dde2;
  }
  * { box-sizing: border-box; margin: 0; padding: 0; }
  html, body {
    width: 1200px; height: 745px; overflow: hidden;
    background: var(--backdrop);
    font-family: "Open Sans", Arial, sans-serif;
  }
  .letterhead {
    position: absolute; left: 351px; top: 20px;
    width: 498px; height: 705px;
    background: var(--paper);
    box-shadow: 0 2px 10px rgba(0,0,0,0.08);
    color: var(--ink);
  }
  .brand-mark {
    position: absolute; left: 46px; top: 58px;
    width: 34px; height: 34px; border-radius: 50%;
    background: var(--blue-mid);
  }
  .wordmark {
    position: absolute; right: 44px; top: 44px;
    font-size: 12px; font-weight: 600; letter-spacing: 1.5px;
    color: var(--wordmark);
  }
  .letter-body {
    position: absolute; left: 52px; top: 140px; width: 360px;
    font-size: 7.4px; line-height: 1.38;
  }
  .recipient { margin-bottom: 9px; }
  .letter-body p.paragraph { margin-bottom: 9px; }
  .closing { margin-top: 4px; }
  .signature {
    display: block; width: 90px; height: 26px; margin: 8px 0 2px 24px;
    background: var(--signature-tone); border-radius: 2px;
  }
  .signer-title { margin-left: 24px; }
  .contact-footer {
    position: absolute; right: 36px; bottom: 40px;
    text-align: right; font-size: 7.4px; font-weight: 700;
    line-height: 1.5; color: var(--blue-bright);
  }
  .contact-footer .contact-line { color: var(--blue-mid); }
</style>
</head>
<body>
  <main class="letterhead">
    <span class="brand-mark" aria-hidden="true"></span>
    <div class="wordmark">BRIGHT HARBOR CORP</div>

    <section class="letter-body">
      <div class="recipient">
        November 1, 2015<br>
        Mr. Alden Pryce<br>
        58 Quillmere Lane<br>
        Harwick, U.K 40218
      </div>
      <p class="salutation">Dear Mr. Pryce</p>
      <p class="paragraph">The first paragraph of a typical business letter is used to state the main point of the letter. Begin with a friendly opening; then quickly transition into the purpose of your letter. Use a couple of sentences to explain the purpose, but do not go in to detail until the next paragraph.</p>
      <p class="paragraph">Beginning with the second paragraph, state the supporting details to justify your purpose. These may take the form of background information, statistics or first-hand accounts. A few short paragraphs within the body of the letter should be enough to support your reasoning. Finally, in the closing paragraph, briefly restate your purpose and why it is important. If the purpose of your letter is related to your employment, consider ending your letter with your contact information and title if it not included on letterhead.</p>
      <p class="paragraph">Finally, in the closing paragraph, briefly restate your purpose and why it is important. If the purpose of your letter is related to your employment, consider ending your letter with your contact information and title if it not included on letterhead. Finally, in the closing paragraph, briefly restate your purpose and why it is important. If the purpose of your letter is related to your employment, consider ending your letter with your contact information and title if it not included on letterhead.</p>
      <p class="paragraph">Finally, in the closing paragraph, briefly restate your purpose and why it is important. If the purpose of your letter is related to your employment, consider ending your letter with your contact information and title if it not included on letterhead. However, if the purpose is informational, think about closing with gratitude for the reader's time.</p>
      <p class="closing">Sincerely,</p>
      <span class="signature" role="img" aria-label="Handwritten signature of the sender"></span>
      <p class="signer-title">President</p>
    </section>

    <footer class="contact-footer">
      <div class="address-line">No.41, 2F, Tarwin Plaza, Melrick Road, Upper Fenwood Gardens, Bangalore 560 017</div>
      <div class="contact-line">Tel: 080 27481930 &nbsp;|&nbsp; Fax: 080 27481931 &nbsp;|&nbsp; Email: query@brightharbor.example</div>
    </footer>
  </main>
</body>
</html>
```